Business Card for a Wedding Films Business

We require a business card design for our business 'Lewis Marrow Wedding Films'. The logo needs to look classy and high end.

Target Market(s)

Wedding Couples

Contact Information for Business Card

Lewis Marrow Wedding Films
07312 605 227
films@lewismarrowreels.com
www.lewismarrowreels.com

Facebook: @lewismarrowweddingfilms
Instagram: @lewismarrowfilms

Font styles to use
Sans Serif

Requirements
Must have
• Social media icons - Facebook and Instagram

```html
<!DOCTYPE html>
<html lang="en">
<head>
<meta charset="utf-8">
<title>Lewis Marrow Wedding Films – Business Card</title>
<link rel="stylesheet" href="https://fonts.googleapis.com/css2?family=Jost:wght@400;500&display=swap">
<style>
  :root {
    --backdrop: #3b3b3d;
    --card-black: #1d1d1d;
    --card-black-deep: #161616;
    --pattern-tone: #222222;
    --gold: #d9a93a;
    --gold-light: #f3d27a;
    --gold-dark: #a8761e;
  }
  * { box-sizing: border-box; margin: 0; padding: 0; }
  html, body {
    width: 1200px;
    height: 1124px;
    overflow: hidden;
    background: var(--backdrop);
    font-family: "Jost", sans-serif;
  }
  .sheet {
    position: relative;
    width: 1200px;
    height: 1124px;
  }
  .card {
    position: absolute;
    left: 230px;
    width: 740px;
    height: 478px;
    background: var(--card-black);
    box-shadow: 0 10px 30px rgba(0,0,0,0.45);
  }
  .card--back { top: 40px; border-bottom: 4px solid var(--gold); border-left: 4px solid var(--gold); }
  .card--front { top: 606px; }

  /* back side */
  .pattern-field {
    position: absolute;
    inset: 0;
    background: linear-gradient(135deg, var(--pattern-tone), var(--card-black-deep));
  }
  .wordmark {
    position: absolute;
    left: 0; right: 0;
    text-align: center;
    color: var(--gold);
    font-weight: 500;
    text-transform: uppercase;
  }
  .card--back .wordmark { top: 184px; }
  .wordmark__name { display: block; font-size: 40px; letter-spacing: 12px; line-height: 1.2; }
  .wordmark__sub { display: block; font-size: 17px; letter-spacing: 11px; margin-top: 10px; }
  .wordmark__dot {
    display: block;
    width: 14px; height: 14px;
    margin: 0 auto 18px;
    background: var(--gold);
    border-radius: 50%;
  }

  /* front side */
  .gold-frame {
    position: absolute;
    inset: 30px;
    border: 3px solid var(--gold);
  }
  .card--front .wordmark { top: 92px; }
  .card--front .wordmark__name { font-size: 30px; letter-spacing: 8px; }
  .card--front .wordmark__sub { font-size: 13px; letter-spacing: 8px; margin-top: 8px; }
  .name-rule {
    position: absolute;
    top: 172px;
    left: 230px;
    width: 280px;
    height: 2px;
    background: var(--gold);
  }
  .contact {
    position: absolute;
    top: 262px;
    left: 70px;
    right: 70px;
    color: var(--gold);
    font-size: 21px;
    font-weight: 400;
  }
  .contact__row { display: flex; justify-content: space-between; margin-bottom: 10px; }
  .contact__row--center { justify-content: center; }
  .contact__item { display: flex; align-items: center; gap: 9px; }
  .contact__icon { width: 18px; height: 18px; flex: none; }
  .contact__badge {
    width: 18px; height: 18px; flex: none;
    border: 2px solid var(--gold);
    border-radius: 50%;
  }
</style>
</head>
<body>
<main class="sheet">

  <section class="card card--back" aria-label="Card back">
    <div class="pattern-field" role="img" aria-label="Faint embossed repeating monogram pattern across the card"></div>
    <div class="wordmark">
      <span class="wordmark__dot"></span>
      <span class="wordmark__name">Lewis Marrow</span>
      <span class="wordmark__sub">Wedding Films</span>
    </div>
  </section>

  <section class="card card--front" aria-label="Card front">
    <div class="gold-frame"></div>
    <div class="wordmark">
      <span class="wordmark__name">Lewis Marrow</span>
      <span class="wordmark__sub">Wedding Films</span>
    </div>
    <div class="name-rule"></div>

    <div class="contact">
      <div class="contact__row contact__row--center">
        <span class="contact__item">
          <svg class="contact__icon" viewBox="0 0 24 24" aria-hidden="true"><path fill="#d9a93a" d="M6.6 10.8a15 15 0 0 0 6.6 6.6l2.2-2.2c.3-.3.7-.4 1-.2 1.1.4 2.3.6 3.6.6.6 0 1 .4 1 1V20c0 .6-.4 1-1 1A17 17 0 0 1 3 4c0-.6.4-1 1-1h3.5c.6 0 1 .4 1 1 0 1.2.2 2.4.6 3.6.1.3 0 .7-.2 1z"/></svg>
          07312 605 227
        </span>
      </div>
      <div class="contact__row">
        <span class="contact__item">
          <svg class="contact__icon" viewBox="0 0 24 24" aria-hidden="true"><rect x="2" y="5" width="20" height="14" fill="none" stroke="#d9a93a" stroke-width="2"/><path d="M2 6l10 7 10-7" fill="none" stroke="#d9a93a" stroke-width="2"/></svg>
          films@lewismarrowreels.com
        </span>
        <span class="contact__item">
          <svg class="contact__icon" viewBox="0 0 24 24" aria-hidden="true"><g fill="none" stroke="#d9a93a" stroke-width="2"><circle cx="12" cy="12" r="10"/><ellipse cx="12" cy="12" rx="4" ry="10"/><path d="M2 12h20"/></g></svg>
          www.lewismarrowreels.com
        </span>
      </div>
      <div class="contact__row">
        <span class="contact__item"><span class="contact__badge"></span>@lewismarrowweddingfilms</span>
        <span class="contact__item"><span class="contact__badge"></span>@lewismarrowfilms</span>
      </div>
    </div>
  </section>

</main>
</body>
</html>
```